Safety Training company business card design

We are after a high quality, professional business card. We are open to a single or double sided card.

The winning designer must provide the card in a format where we can easily change the name and details of the different people in our organization.

Harbor Guard's company colour is lime green.

We provide all aspects of safety advisory and training for the Building, Civil Construction, Mining, Oil and Gas, Manufacturing, Rail, Rural and Retail sectors.

Visit our website www.harborguard.com.au for training competencies we offer along with our other services including RPL's, safety audits, professional development and client support.

Target Market(s)

Those in the Building, Civil Construction, Mining, Oil and Gas, Manufacturing, Rail, Rural and Retail industries.

Industry/Entity Type

Training

Contact Information for Business Card

Harbor Guard
Safety and Training
Dennis Palworth
Director
M 0427 518 266
dennis@harborguard.com.au
www.harborguard.com.au
(2 business addresses:)
Corvin High Risk Training Centre
17 Tandem Parade, Ashgrove Point Q 4218 P 3912 5486 F 3912 5174
Brenlow Training Centre
86 Fenwick Street, Kestrel Vale Q 4815 P 4873 2615 F 4873 2249

Colors
9bcb3c

Requirements
Must have
• Lime green must be the main colour. must include HG logo attached, and state Harbor Guard (Safety and Training in smaller/different font).

State something along the lines of:

Nice to have
• We offer remote training and we can come to you.

```html
<!DOCTYPE html>
<html lang="en">
<head>
<meta charset="utf-8">
<title>Harbor Guard – Business Card</title>
<link href="https://fonts.googleapis.com/css2?family=Arimo:wght@400;700&display=swap" rel="stylesheet">
<style>
  :root {
    --lime: #9bcb3c;
    --red: #c8322a;
    --ink: #3a3a3a;
    --rule: #8a8a8a;
    --paper: #ffffff;
    --stage: #e6e8e4;
    --band-text: #f4f7e8;
  }
  html, body {
    margin: 0;
    padding: 0;
    width: 1200px;
    height: 900px;
    overflow: hidden;
    background: var(--stage);
    font-family: "Arimo", Arial, sans-serif;
  }
  .canvas {
    position: relative;
    width: 1200px;
    height: 900px;
  }
  .card {
    position: absolute;
    left: 290px;
    width: 620px;
    height: 379px;
    background: var(--paper);
    box-shadow: 0 6px 18px rgba(0,0,0,0.18);
    overflow: hidden;
  }
  .card--back { top: 46px; }
  .card--front { top: 475px; }

  .band {
    position: absolute;
    left: 0;
    width: 100%;
    background: var(--lime);
    border-top: 2px solid var(--red);
    border-bottom: 2px solid var(--red);
    box-sizing: border-box;
  }

  /* wordmark */
  .wordmark {
    display: flex;
    align-items: center;
    gap: 10px;
  }
  .wordmark__dot {
    width: 28px;
    height: 28px;
    border-radius: 50%;
    background: var(--red);
    flex: none;
  }
  .wordmark__name {
    font-weight: 700;
    font-size: 34px;
    letter-spacing: 1px;
    text-transform: uppercase;
    color: var(--red);
    white-space: nowrap;
  }
  .wordmark__sub {
    font-size: 10px;
    letter-spacing: 4px;
    text-transform: uppercase;
    color: var(--band-text);
    margin: 4px 0 0 38px;
  }

  /* back */
  .card--back .wordmark-block {
    position: absolute;
    left: 120px;
    top: 124px;
  }
  .card--back .wordmark__dot { width: 34px; height: 34px; }
  .card--back .wordmark__name { font-size: 44px; }
  .card--back .band {
    top: 262px;
    height: 68px;
    display: flex;
    align-items: center;
    justify-content: center;
  }
  .tagline {
    margin: 0;
    padding: 0 36px;
    font-size: 13px;
    line-height: 1.45;
    color: var(--ink);
    text-align: center;
  }

  /* front */
  .card--front .band--head {
    top: 18px;
    height: 92px;
    padding: 18px 0 0 26px;
  }
  .card--front .band--foot {
    top: 336px;
    height: 26px;
  }
  .person {
    position: absolute;
    left: 0;
    top: 132px;
    padding-left: 22px;
    border-left: 5px solid var(--red);
  }
  .person__name {
    margin: 0;
    font-size: 19px;
    font-weight: 700;
    letter-spacing: 0.5px;
    text-transform: uppercase;
    color: var(--red);
  }
  .person__role {
    font-weight: 400;
    font-size: 14px;
    color: var(--ink);
  }
  .person__org {
    margin: 4px 0 0;
    font-size: 14px;
    letter-spacing: 1px;
    text-transform: uppercase;
    color: var(--ink);
  }
  .rule {
    position: absolute;
    left: 26px;
    right: 26px;
    top: 190px;
    height: 1px;
    background: var(--rule);
  }
  .contacts {
    position: absolute;
    left: 26px;
    top: 262px;
    margin: 0;
    padding: 0;
    list-style: none;
    font-size: 13px;
    letter-spacing: 0.6px;
    color: var(--ink);
  }
  .contacts li {
    display: flex;
    align-items: center;
    gap: 10px;
    height: 20px;
  }
  .icon { width: 11px; height: 11px; fill: var(--red); flex: none; }
  .sites {
    position: absolute;
    right: 26px;
    top: 204px;
    text-align: right;
    font-size: 13px;
    line-height: 20px;
    color: var(--ink);
  }
  .site { margin: 0 0 4px; }
  .site__title { display: inline-flex; align-items: center; gap: 6px; }
</style>
</head>
<body>
<main class="canvas">

  <section class="card card--back" aria-label="Card back">
    <div class="wordmark-block">
      <div class="wordmark">
        <span class="wordmark__dot"></span>
        <span class="wordmark__name">Harbor Guard</span>
      </div>
    </div>
    <div class="band">
      <p class="tagline">We provide all aspects of safety advisory and training for the Building, Civil Construction, Mining, Oil and Gas, Manufacturing, Rail, Rural and Retail sectors</p>
    </div>
  </section>

  <section class="card card--front" aria-label="Card front">
    <div class="band band--head">
      <div class="wordmark">
        <span class="wordmark__dot"></span>
        <span class="wordmark__name">Harbor Guard</span>
      </div>
      <div class="wordmark__sub">Safety and Training</div>
    </div>

    <div class="person">
      <h1 class="person__name">Dennis Palworth <span class="person__role">/DIRECTOR</span></h1>
      <p class="person__org">Harbor Guard Safety and Training</p>
    </div>

    <div class="rule"></div>

    <div class="sites">
      <p class="site">
        <span class="site__title">Brenlow Training Centre 86 Fenwick Street
          <svg class="icon" viewBox="0 0 12 12"><path d="M6 1 L11 6 H9.5 V11 H7 V8 H5 V11 H2.5 V6 H1 Z"/></svg>
        </span><br>
        Kestrel Vale Q 4815 P 4873 2615 F 4873 2249
      </p>
      <p class="site">
        <span class="site__title">Corvin High Risk Training Centre 17 Tandem Parade
          <svg class="icon" viewBox="0 0 12 12"><path d="M6 1 L11 6 H9.5 V11 H7 V8 H5 V11 H2.5 V6 H1 Z"/></svg>
        </span><br>
        Ashgrove Point Q 4218 P 3912 5486 F 3912 5174
      </p>
    </div>

    <ul class="contacts">
      <li>
        <svg class="icon" viewBox="0 0 12 12"><rect x="3" y="0.5" width="6" height="11" rx="1.2"/></svg>
        0427 518 266
      </li>
      <li>
        <svg class="icon" viewBox="0 0 12 12"><path d="M0.5 2.5 H11.5 V9.5 H0.5 Z M1 3 L6 7 L11 3" fill="none" stroke="#c8322a" stroke-width="1.2"/></svg>
        dennis@harborguard.com.au
      </li>
      <li>
        <svg class="icon" viewBox="0 0 12 12"><g fill="none" stroke="#c8322a" stroke-width="1.1"><circle cx="6" cy="6" r="5"/><ellipse cx="6" cy="6" rx="2.2" ry="5"/><path d="M1 6 H11"/></g></svg>
        www.harborguard.com.au
      </li>
    </ul>

    <div class="band band--foot"></div>
  </section>

</main>
</body>
</html>
```